Loopnest Ad Image for Ebook

I need someone to design a good looking loopnest ad image for my ebook. Must comply with Loopnest ad police and generate lots of clicks and opt ins. Use my 3d cover attached.

```html
<!DOCTYPE html>
<html lang="en">
<head>
<meta charset="utf-8">
<title>The Steady Posting Blueprint – Ad</title>
<link rel="stylesheet" href="https://fonts.googleapis.com/css2?family=Oswald:wght@500&family=Roboto+Condensed:ital,wght@1,700&family=Montserrat:wght@300;500;600&display=swap">
<style>
  :root {
    --brand-blue: #1a7cc6;
    --deep-blue: #0d5fa8;
    --ink: #0b0b0c;
    --white: #ffffff;
    --accent-red: #ff2b1e;
    --button-top: #a9dcf7;
    --button-bottom: #4bb0e8;
    --photo-dark: #1d2c3a;
    --photo-mid: #4b6378;
    --photo-light: #b9c4cc;
    --cover-photo-top: #f1f2f3;
    --cover-photo-bottom: #c9ced3;
  }
  * { box-sizing: border-box; margin: 0; padding: 0; }
  html, body { width: 1200px; height: 717px; overflow: hidden; background: #d0d0d0; }

  .ad {
    position: relative;
    width: 1200px;
    height: 717px;
    overflow: hidden;
    background: var(--photo-dark);
  }

  .hero-photo {
    position: absolute;
    inset: 0;
    background:
      radial-gradient(ellipse 40% 30% at 70% 60%, rgba(220,180,160,0.45), transparent 70%),
      linear-gradient(160deg, var(--photo-light) 0%, var(--photo-mid) 35%, var(--photo-dark) 75%, #3a2a22 100%);
  }

  .corner-wedge { position: absolute; inset: 0; }

  .title-band {
    position: absolute;
    left: 0; top: 82px;
    width: 767px; height: 58px;
    background: var(--ink);
    clip-path: polygon(56px 0, 100% 0, 100% 100%, 0 100%);
    display: flex; align-items: center; justify-content: center;
    padding-left: 60px;
    font-family: "Roboto Condensed", "Arial Narrow", sans-serif;
    font-style: italic; font-weight: 700;
    font-size: 46px; color: var(--white);
    letter-spacing: 0.5px;
    white-space: nowrap;
  }

  .offer-band {
    position: absolute;
    left: 0; top: 140px;
    width: 767px; height: 109px;
    background: linear-gradient(90deg, #1e87d0, var(--brand-blue));
    display: flex; align-items: center;
    padding-left: 80px;
    font-family: "Oswald", "Arial Narrow", sans-serif;
    font-weight: 500; font-size: 62px;
    color: var(--white);
    letter-spacing: 1px;
    white-space: nowrap;
  }
  .offer-band .highlight { color: var(--accent-red); }

  .cta-button {
    position: absolute;
    left: 164px; top: 556px;
    width: 344px; height: 110px;
    border-radius: 14px;
    background: linear-gradient(180deg, var(--button-top), var(--button-bottom));
    border: 3px solid #2a8fd2;
    box-shadow: 0 6px 14px rgba(0,0,0,0.35);
    display: flex; align-items: center; justify-content: center;
    padding-left: 40px;
    font-family: "Oswald", "Arial Narrow", sans-serif;
    font-weight: 500; font-size: 38px; color: var(--white);
    letter-spacing: 0.5px;
  }
  .cta-pointer { position: absolute; left: 104px; top: 556px; width: 100px; height: 150px; }

  .ebook {
    position: absolute;
    left: 764px; top: 29px;
    width: 340px; height: 664px;
    box-shadow: 8px 10px 22px rgba(0,0,0,0.45);
    background: var(--ink);
  }
  .ebook-art { position: absolute; inset: 0; }
  .ebook-title {
    position: absolute;
    left: 25px; top: 467px;
    font-family: "Montserrat", Arial, sans-serif;
    font-weight: 300; font-size: 22px; line-height: 30px;
    color: var(--white);
  }
  .ebook-title .emphasis {
    display: block;
    font-weight: 500; font-size: 28px; line-height: 38px;
    color: #2e9de6;
    letter-spacing: 0.5px;
  }
  .ebook-publisher {
    position: absolute;
    left: 176px; top: 600px;
    display: flex; align-items: center; gap: 8px;
    font-family: "Montserrat", Arial, sans-serif;
    font-weight: 600; font-size: 13px; line-height: 15px;
    color: var(--ink);
    text-transform: uppercase;
  }
  .ebook-publisher .mark { width: 14px; height: 14px; background: var(--ink); flex: none; }
</style>
</head>
<body>
  <main class="ad">
    <div class="hero-photo" role="img" aria-label="Blurred photo of hands typing on a laptop keyboard"></div>

    <svg class="corner-wedge" width="1200" height="717" viewBox="0 0 1200 717" aria-hidden="true">
      <polygon points="585,717 1133,0 1200,0 1200,717" fill="var(--brand-blue)"/>
    </svg>

    <div class="title-band">THE STEADY POSTING</div>
    <div class="offer-band">GET THIS&nbsp;<span class="highlight">FREE</span>&nbsp;BLUEPRINT</div>

    <a class="cta-button">CLICK HERE</a>
    <svg class="cta-pointer" viewBox="0 0 100 150" aria-hidden="true">
      <path d="M38 14 c0-10 16-10 16 0 v46 l30 8 c8 2 12 8 11 16 l-5 34 c-2 10-8 16-18 16 h-30 c-8 0-12-4-16-10 l-20-30 c-4-6 2-14 10-10 l22 14 z"
            fill="var(--white)" stroke="var(--deep-blue)" stroke-width="7" stroke-linejoin="round"/>
    </svg>

    <section class="ebook" aria-label="The Steady Posting Blueprint ebook cover">
      <svg class="ebook-art" width="340" height="664" viewBox="0 0 340 664">
        <defs>
          <linearGradient id="cover-photo" x1="0" y1="0" x2="0" y2="1">
            <stop offset="0" stop-color="var(--cover-photo-top)"/>
            <stop offset="1" stop-color="var(--cover-photo-bottom)"/>
          </linearGradient>
        </defs>
        <rect width="340" height="405" fill="url(#cover-photo)" role="img" aria-label="Photo of a person working on a laptop showing a blog page"/>
        <polygon points="0,358 231,405 127,664 0,664" fill="var(--ink)"/>
        <polygon points="231,405 340,319 340,452" fill="var(--brand-blue)"/>
        <polygon points="127,664 231,405 340,452 340,664" fill="var(--white)"/>
      </svg>
      <h2 class="ebook-title">THE STEADY<br>POSTING<span class="emphasis">BLUEPRINT</span></h2>
      <div class="ebook-publisher"><span class="mark"></span><span>Harborline<br>Media</span></div>
    </section>
  </main>
</body>
</html>
```